Front & Back cover design for timber flooring brochure - A4 size

I need a design for the front and back cover of an A4 sized brochure for a timber and concrete flooring company called "Kestrel Row Floors". The front cover should include the logo (attached), and an image + tagline for each of the three products/services that they offer which are:

1. Timber Flooring
2. Concrete Grinding & Sealing
3. Floor sanding (i have attached a photo for each of these three - however feel free to use other images if you feel they are better).

The back cover should be simple, perhaps just a continuation of the colour or graphic scheme on the front with the company contact details at the bottom.

Industry/Entity Type

Flooring

Requirements
Must have
• front cover has to have the logo with an image and text of the 3 services described. You can use the images attached or your own.

```html
<!DOCTYPE html>
<html lang="en">
<head>
<meta charset="utf-8">
<title>Kestrel Row Floors – Brochure Cover</title>
<link rel="stylesheet" href="https://fonts.googleapis.com/css2?family=Crimson+Text:wght@400;600&display=swap">
<style>
  :root {
    --wood-light: #a0621f;
    --wood-mid: #915719;
    --wood-dark: #7c4814;
    --panel-shadow: #3e2210;
    --seam: #4a2c12;
    --accent-bar: #5a2a22;
    --timber-top: #6e2e22;
    --timber-bottom: #7a3a24;
    --concrete-top: #a3a89c;
    --concrete-bottom: #6d7364;
    --sanding-top: #d06a2a;
    --sanding-bottom: #9c3c18;
    --label: #d3b07e;
    --address: #dcc09a;
    --contact: #ecd9bd;
    --logo-small: #d89a3c;
    --logo-large: #3a1408;
    --logo-square: #8c1a14;
  }
  * { margin: 0; padding: 0; box-sizing: border-box; }
  html, body { width: 1200px; height: 837px; overflow: hidden; background: #fff; }
  .cover {
    position: relative;
    width: 1200px;
    height: 837px;
    font-family: "Crimson Text", Georgia, serif;
  }
  .cover__art { position: absolute; inset: 0; }
  .back-logo {
    position: absolute;
    left: 187px; top: 590px;
    display: flex; align-items: center; gap: 6px;
    color: var(--logo-small);
    font-size: 14px; font-weight: 400;
    text-transform: uppercase; letter-spacing: 0.5px;
  }
  .back-logo__square { width: 14px; height: 14px; background: var(--logo-small); }
  .address {
    position: absolute;
    left: 188px; top: 640px;
    color: var(--address);
    font-size: 14.5px; line-height: 16.6px;
    list-style: none;
  }
  .contact {
    position: absolute;
    left: 187px; top: 737px;
    color: var(--contact);
    font-size: 12px; font-weight: 600; line-height: 14.5px;
    list-style: none;
  }
  .service-label {
    position: absolute;
    top: 563px;
    color: var(--label);
    font-size: 12.5px; line-height: 14.5px;
  }
  .service-label--timber { left: 787px; }
  .service-label--concrete { left: 904px; }
  .service-label--sanding { left: 1024px; }
  .front-logo {
    position: absolute;
    left: 772px; top: 700px;
    width: 378px;
    display: flex; align-items: center; justify-content: center; gap: 12px;
    color: var(--logo-large);
    font-size: 30px; font-weight: 600;
    text-transform: uppercase; letter-spacing: 1px;
    white-space: nowrap;
  }
  .front-logo__square { width: 38px; height: 38px; background: var(--logo-square); flex: none; }
</style>
</head>
<body>
<main class="cover">
  <svg class="cover__art" width="1200" height="837" viewBox="0 0 1200 837">
    <defs>
      <linearGradient id="wood" x1="0" y1="0" x2="1" y2="0">
        <stop offset="0" stop-color="var(--wood-dark)"/>
        <stop offset="0.3" stop-color="var(--wood-light)"/>
        <stop offset="0.6" stop-color="var(--wood-mid)"/>
        <stop offset="1" stop-color="var(--wood-light)"/>
      </linearGradient>
      <linearGradient id="timber" x1="0" y1="0" x2="0" y2="1">
        <stop offset="0" stop-color="var(--timber-top)"/>
        <stop offset="0.8" stop-color="var(--timber-bottom)"/>
        <stop offset="1" stop-color="var(--timber-bottom)" stop-opacity="0"/>
      </linearGradient>
      <linearGradient id="concrete" x1="0" y1="0" x2="0" y2="1">
        <stop offset="0" stop-color="var(--concrete-top)"/>
        <stop offset="0.8" stop-color="var(--concrete-bottom)"/>
        <stop offset="1" stop-color="var(--concrete-bottom)" stop-opacity="0"/>
      </linearGradient>
      <linearGradient id="sanding" x1="0" y1="0" x2="0" y2="1">
        <stop offset="0" stop-color="var(--sanding-top)"/>
        <stop offset="0.8" stop-color="var(--sanding-bottom)"/>
        <stop offset="1" stop-color="var(--sanding-bottom)" stop-opacity="0"/>
      </linearGradient>
    </defs>

    <rect class="wood-surface" width="1200" height="837" fill="url(#wood)" role="img" aria-label="Warm timber board photograph covering both covers"/>

    <line class="board-seam" x1="133" y1="0" x2="133" y2="837" stroke="var(--seam)" stroke-width="2"/>
    <line class="spine" x1="715" y1="0" x2="715" y2="837" stroke="var(--seam)" stroke-width="2"/>
    <rect class="accent-bar" x="60" y="648" width="71" height="9" fill="var(--accent-bar)"/>

    <path class="back-wave" d="M158 0 H308 C300 200 335 420 318 600 C310 700 322 780 325 837 H180 C176 700 190 560 170 420 C150 260 172 120 158 0 Z" fill="var(--panel-shadow)" opacity="0.55"/>

    <path class="service-image service-image--timber" role="img" aria-label="Photograph of dark timber flooring" d="M796 0 H908 C900 150 918 320 912 460 C908 540 915 580 912 610 H778 C780 520 786 430 778 330 C772 200 800 110 796 0 Z" fill="url(#timber)"/>
    <path class="service-image service-image--concrete" role="img" aria-label="Photograph of polished concrete floor" d="M912 0 H1024 C1030 150 1020 320 1030 460 C1034 540 1025 580 1028 610 H896 C900 520 896 430 900 330 C904 200 918 110 912 0 Z" fill="url(#concrete)"/>
    <path class="service-image service-image--sanding" role="img" aria-label="Photograph of freshly sanded timber floorboards" d="M1030 0 H1146 C1140 150 1156 320 1146 460 C1140 540 1146 580 1144 610 H1016 C1022 520 1012 430 1020 330 C1028 200 1036 110 1030 0 Z" fill="url(#sanding)"/>
  </svg>

  <div class="back-logo"><span class="back-logo__square"></span>Kestrel Row Floors</div>
  <ul class="address">
    <li>Showroom</li>
    <li>Streetname</li>
    <li>Townname</li>
    <li>County</li>
    <li>Postcode</li>
  </ul>
  <ul class="contact">
    <li>Tel: 020 7946 0381</li>
    <li>Fax: 020 7946 0381</li>
    <li>Email: info@kestrelrowfloors.co.uk</li>
  </ul>

  <p class="service-label service-label--timber">Timber<br>Flooring</p>
  <p class="service-label service-label--concrete">Concrete Grinding<br>and Sealing</p>
  <p class="service-label service-label--sanding">Floor<br>Sanding</p>

  <div class="front-logo"><span class="front-logo__square"></span>Kestrel Row Floors</div>
</main>
</body>
</html>
```